Hochzeitseinladung im Pocketfold-Style
Zielgruppe
Vertrieb von Hochzeitspapeterie. Unsere Zielgruppe ist weiblich, verlobt, 20 - 40 Jahre alt.
Aufgabenstellung
Wir benötigen ein Design für die Einladungskarte + Einleger in einen Pocketfoldumschlag (Umschlag soll nicht gestaltet werden).
EINLADUNGSTEXT
Formate in mm:130x130mm
Vorgabe für Design / Layout:
Schlichtes Design ohne aufwendige Grafiken mit leichtem Hauch zum Vintage ("Vintage Wedding Icons" z.B. Girlande, Zweig, Retro-Icons wie Vintage Fahrrad, Vogelkäfig, Lampions, etc).
Evtl. oben Initialen C und S unterbringen
Schrift: Farbe dunkelgrau, Font (nur lizenzfreie)
Keine Verwendung von Sonderfarben
Farben Dokument gesamt incl. Grafiken und Objekten: Max. 3 Farben (z.b. Mix aus Grau, Koralle, Altrosa, Mint)
Keine Fotos
EINLEGER
3 x Format in mm: 130x130mm
- Hier nur ein Design für die Überschrift passend zum Einladungsdesign
(3 Überschriften: Unser Tag + Hotel & Anreise + RSVP/Antwort)
Abnahme:
Designbeispiele als pdf zur Korrektur/Abnahme
Fertiges Design soll am Ende als InDesign File sowie als druckfähige pdf-Datei an Käufer gesendet werden.
Vom Gewinner-Design gehen alle Rechte zur kommerziellen Nutzung an den Käufer über.

```html
<!DOCTYPE html>
<html lang="de">
<head>
<meta charset="utf-8">
<title>Hochzeitseinladung – Pocketfold</title>
<link rel="stylesheet" href="https://fonts.googleapis.com/css2?family=Parisienne&family=Petit+Formal+Script&family=Great+Vibes&display=swap">
<style>
  :root {
    --ink: #3a3837;
    --band: #565251;
    --rose: #e2287c;
    --mint: #8fd3b0;
    --mint-soft: #d6f0e2;
    --rose-soft: #f7d3e2;
    --paper: #ffffff;
    --stage: #ebe7e1;
  }
  * { box-sizing: border-box; margin: 0; padding: 0; }
  html, body { width: 1200px; height: 696px; overflow: hidden; }
  body {
    background: var(--stage);
    font-family: "Petit Formal Script", cursive;
    color: var(--ink);
    position: relative;
  }

  /* Invitation card */
  .invitation {
    position: absolute;
    left: 300px; top: 36px;
    width: 420px; height: 624px;
    background: var(--paper);
    box-shadow: 0 2px 8px rgba(0,0,0,.12);
    overflow: hidden;
  }
  .floral-frame {
    position: absolute; inset: 0;
    background:
      radial-gradient(circle at 8% 6%, var(--mint) 0 40px, transparent 70px),
      radial-gradient(circle at 96% 20%, var(--rose-soft) 0 30px, transparent 60px),
      radial-gradient(circle at 96% 45%, var(--rose-soft) 0 26px, transparent 55px),
      radial-gradient(circle at 4% 40%, var(--mint) 0 30px, transparent 60px),
      radial-gradient(circle at 20% 98%, var(--rose-soft) 0 40px, transparent 70px),
      radial-gradient(circle at 70% 99%, var(--mint) 0 30px, transparent 60px),
      radial-gradient(circle at 95% 90%, var(--mint) 0 30px, transparent 60px),
      linear-gradient(var(--mint-soft), var(--rose-soft));
  }
  .card-panel {
    position: absolute;
    left: 24px; right: 24px; top: 16px; bottom: 42px;
    background: var(--paper);
  }

  .monogram {
    position: absolute; left: 0; right: 0; top: 28px;
    text-align: center;
  }
  .flourish {
    width: 120px; height: 12px; margin: 0 auto;
    background: linear-gradient(90deg, transparent, #dcdad8, transparent);
    border-radius: 6px;
  }
  .couple-name {
    font-family: "Parisienne", cursive;
    font-size: 46px; line-height: 48px; color: var(--ink);
  }
  .ampersand { font-family: "Parisienne", cursive; font-size: 30px; line-height: 24px; }
  .ribbon {
    display: inline-block;
    margin: 2px 0;
    padding: 2px 30px;
    border-top: 1.5px solid var(--ink);
    border-bottom: 1.5px solid var(--ink);
    font-family: "Great Vibes", cursive;
    font-size: 20px; color: var(--rose);
  }

  .invite-lines {
    position: absolute; left: 0; right: 0; top: 226px;
    text-align: center; line-height: 1.35;
  }
  .invite-lines .lead { font-size: 19px; }
  .invite-lines .event { font-size: 23px; }
  .invite-lines .place { font-size: 17px; }
  .invite-lines .date { font-size: 15px; }

  .schedule-band {
    position: absolute; left: 0; right: 0; top: 362px; height: 44px;
    background: var(--band);
    color: #fff;
    font-size: 9px; line-height: 12px;
  }
  .schedule-item { position: absolute; top: 7px; }
  .schedule-item small { display: block; font-size: 7px; line-height: 10px; opacity: .85; }
  .schedule-item.ceremony { left: 58px; }
  .schedule-item.dinner { left: 262px; }
  .emblem {
    position: absolute; left: 180px; top: 348px;
    width: 60px; height: 72px;
    border: 2px solid var(--rose);
    border-radius: 10px;
    background: var(--band);
  }

  .closing {
    position: absolute; left: 0; right: 0; top: 440px;
    text-align: center;
  }
  .closing .note { font-size: 9px; line-height: 14px; }
  .closing .reply { font-size: 15px; margin: 10px 0 12px; }
  .closing .contact { font-size: 8px; line-height: 13px; }

  /* Inserts */
  .insert {
    position: absolute;
    left: 770px; width: 200px; height: 200px;
    background: var(--paper);
    box-shadow: 0 2px 8px rgba(0,0,0,.12);
    overflow: hidden;
  }
  .insert.our-day { top: 36px; }
  .insert.hotel { top: 248px; }
  .insert.reply-card { top: 460px; }
  .insert-floral {
    position: absolute; left: 0; top: 0; bottom: 0; width: 14px;
    background: linear-gradient(180deg, var(--mint), var(--mint-soft), var(--rose-soft));
  }
  .insert-floral.bottom {
    width: auto; height: 14px; top: auto; right: 0;
    background: linear-gradient(90deg, var(--mint), var(--rose-soft));
  }
  .insert-heading {
    position: absolute; left: 14px; right: 0; top: 62px;
    text-align: center;
  }
  .insert-heading .flourish { width: 90px; height: 10px; }
  .insert-heading h2 {
    font-family: "Petit Formal Script", cursive;
    font-weight: 400; font-size: 20px; line-height: 28px;
    margin: 12px 0; white-space: nowrap;
    color: var(--ink);
  }
</style>
</head>
<body>

<article class="invitation">
  <div class="floral-frame" role="img" aria-label="Aquarellblumen und Blätter in Mint und Rosé als Rahmen"></div>
  <div class="card-panel">
    <header class="monogram">
      <div class="flourish" role="img" aria-label="Geschwungene Zierlinie"></div>
      <div class="couple-name">Clara</div>
      <div class="ribbon">Save the Date</div>
      <div class="ampersand">&amp;</div>
      <div class="couple-name">Simon</div>
      <div class="flourish" role="img" aria-label="Geschwungene Zierlinie"></div>
    </header>

    <section class="invite-lines">
      <p class="lead">Come away with us</p>
      <p class="event">to a Wedding Weekend</p>
      <p class="place">in The Wolds, England</p>
      <p class="date">09. Juli 2017/Sonntag</p>
    </section>

    <section class="closing">
      <p class="note">Wir feiern unsere Hochzeit und möchten diesen<br>schönen Moment gerne mit Euch gemeinsam erleben.</p>
      <p class="reply">Antwort bitte bis 31.März</p>
      <p class="contact">Familie Brenninger | Lindenweg 4 | 54321 Talheim<br>hallo@clara-und-simon.de | +49 30 555 0182</p>
    </section>
  </div>

  <div class="schedule-band">
    <div class="schedule-item ceremony">14.00 Zeremonie<small>The Manor House</small><small>in Lower Village</small></div>
    <div class="schedule-item dinner">18.30 Restaurant/Hotel<small>The Fernley</small><small>in Stowerd</small></div>
  </div>
  <div class="emblem" role="img" aria-label="Rosa Zierrahmen mit Tulpenmotiv"></div>
</article>

<article class="insert our-day">
  <div class="insert-floral" role="img" aria-label="Aquarellblätter am Rand"></div>
  <div class="insert-heading">
    <div class="flourish" role="img" aria-label="Geschwungene Zierlinie"></div>
    <h2>Unser Tag</h2>
    <div class="flourish" role="img" aria-label="Geschwungene Zierlinie"></div>
  </div>
</article>

<article class="insert hotel">
  <div class="insert-floral" role="img" aria-label="Aquarellblätter am Rand"></div>
  <div class="insert-heading">
    <div class="flourish" role="img" aria-label="Geschwungene Zierlinie"></div>
    <h2>Hotel &amp; Anreise</h2>
    <div class="flourish" role="img" aria-label="Geschwungene Zierlinie"></div>
  </div>
</article>

<article class="insert reply-card">
  <div class="insert-floral" role="img" aria-label="Aquarellblätter am Rand"></div>
  <div class="insert-floral bottom" role="img" aria-label="Aquarellblumen am unteren Rand"></div>
  <div class="insert-heading">
    <div class="flourish" role="img" aria-label="Geschwungene Zierlinie"></div>
    <h2>RSVP / Antwort</h2>
    <div class="flourish" role="img" aria-label="Geschwungene Zierlinie"></div>
  </div>
</article>

</body>
</html>
```